Business Card Design

It is an assisted living facility. I wanted the name to reflect that we are a step above other facilities; i.e., professionally decorated rooms, cloth napkins, family dinners, etc. My motto is: COME WHERE YOU ARE CELEBRATED! Also, I have thought about having a house held with the "Hands" and the motto around it but I have seen that logo used other places. In other words, HELP!

I do not have a photo yet, but the photographer is coming next week. I would like the back of the card to have a picture of the facility.

Industry/Entity Type

Business

Contact Information for Business Card

BRIGHT MEADOW ASSISTED LIVING, LLC, 2938 Quillmont Dr., FL 33482-7261
Phone: (555) 214-6037; Fax: (555)
Linda Pruett, Owner/Administrator

```html
<!DOCTYPE html>
<html lang="en">
<head>
<meta charset="utf-8">
<title>Bright Meadow Assisted Living — Business Card</title>
<link rel="stylesheet" href="https://fonts.googleapis.com/css2?family=Open+Sans:wght@400;600;700&display=swap">
<style>
  :root {
    --backdrop: #ece9e4;
    --card: #ffffff;
    --ink: #3a3a3c;
    --charcoal: #2f2f31;
    --crimson: #d0203a;
    --stripe: #e4e4e4;
    --stripe-bg: #f4f4f4;
  }
  * { margin: 0; padding: 0; box-sizing: border-box; }
  html, body {
    width: 1200px; height: 1108px; overflow: hidden;
    background: var(--backdrop);
    font-family: "Open Sans", Arial, sans-serif;
  }
  .card {
    position: absolute; left: 160px;
    width: 880px; height: 500px;
    background: var(--card);
    box-shadow: 0 6px 18px rgba(0,0,0,.18);
    overflow: hidden;
  }
  .card--back { top: 36px; }
  .card--front { top: 572px; }
  .card__shapes { position: absolute; left: 0; top: 0; width: 880px; height: 500px; }

  .back__company {
    position: absolute; left: 0; right: 0; top: 200px;
    text-align: center; padding-left: 60px;
    color: var(--ink); font-size: 30px; font-weight: 600; letter-spacing: .3px;
  }

  .namebox {
    position: absolute; left: 481px; top: 116px; width: 346px; height: 93px;
    background: repeating-linear-gradient(135deg, var(--stripe) 0 2px, var(--stripe-bg) 2px 6px);
    clip-path: polygon(0 0, 100% 0, 100% 100%, 22% 100%);
  }
  .namebox__accent {
    position: absolute; left: 827px; top: 116px; width: 53px; height: 93px;
    background: var(--crimson);
  }
  .person {
    position: absolute; right: 85px; top: 124px; text-align: right;
  }
  .person__name { font-size: 34px; color: var(--ink); font-weight: 400; line-height: 1.2; }
  .person__name strong { font-weight: 700; }
  .person__title { font-size: 15px; color: var(--crimson); font-weight: 600; line-height: 1.2; }

  .front__company {
    position: absolute; left: 58px; top: 240px;
    font-size: 26px; font-weight: 600; color: var(--crimson); letter-spacing: .2px;
  }
  .address {
    position: absolute; left: 58px; top: 384px;
    font-size: 19px; color: var(--ink);
    display: flex; align-items: center; gap: 8px;
  }
  .contact {
    position: absolute; right: 64px; font-size: 19px; color: var(--ink);
    display: flex; align-items: center; gap: 10px;
  }
  .contact--fax { top: 366px; }
  .contact--phone { top: 405px; }
  .icon { display: block; }
</style>
</head>
<body>

<section class="card card--back" aria-label="Card back">
  <svg class="card__shapes" viewBox="0 0 880 500" aria-hidden="true">
    <polygon points="610,430 880,430 880,500 650,500" fill="var(--crimson)"/>
    <polygon points="230,500 470,385 640,385 720,500" fill="var(--charcoal)"/>
  </svg>
  <p class="back__company">BRIGHT MEADOW ASSISTED LIVING, LLC</p>
</section>

<section class="card card--front" aria-label="Card front">
  <svg class="card__shapes" viewBox="0 0 880 500" aria-hidden="true">
    <rect x="300" y="447" width="580" height="53" fill="var(--crimson)"/>
    <polygon points="0,411 355,411 440,500 0,500" fill="var(--charcoal)"/>
  </svg>

  <div class="namebox"></div>
  <div class="namebox__accent"></div>
  <div class="person">
    <p class="person__name"><strong>Linda</strong> Pruett</p>
    <p class="person__title">OWNER/ADMINISTRATOR</p>
  </div>

  <p class="front__company">BRIGHT MEADOW ASSISTED LIVING, LLC</p>

  <p class="address">
    <svg class="icon" width="12" height="18" viewBox="0 0 12 18" aria-hidden="true">
      <path d="M6 0a6 6 0 0 0-6 6c0 4.5 6 12 6 12s6-7.5 6-12a6 6 0 0 0-6-6z" fill="var(--crimson)"/>
      <circle cx="6" cy="6" r="2.3" fill="#fff"/>
    </svg>
    2938 Quillmont Dr., FL 33482-7261
  </p>

  <p class="contact contact--fax">
    (555)
    <svg class="icon" width="20" height="17" viewBox="0 0 20 17" aria-hidden="true">
      <rect x="5" y="0" width="10" height="5" fill="var(--crimson)"/>
      <rect x="0" y="5" width="20" height="8" rx="1.5" fill="var(--crimson)"/>
      <rect x="5" y="10" width="10" height="7" fill="var(--crimson)" stroke="#fff" stroke-width="1.5"/>
    </svg>
  </p>
  <p class="contact contact--phone">
    (555) 214-6037
    <svg class="icon" width="20" height="16" viewBox="0 0 20 16" aria-hidden="true">
      <path d="M1 5c0-3 4-4 9-4s9 1 9 4v2h-5V5H6v2H1z" fill="var(--crimson)"/>
      <path d="M4 8h12l2 8H2z" fill="var(--crimson)"/>
      <circle cx="10" cy="12" r="2" fill="#fff"/>
    </svg>
  </p>
</section>

</body>
</html>
```